Marine Business Card

We install Lighting, Sound, Video, PA Systems to hotels, nightclubs, Restaurants, Cruise Ships.

Target Market(s)

We want to focus on the Marine or Maritime/Cruise industry. Passenger ships and cruise liners are the companies we want to appeal to

Industry/Entity Type

Business

Contact Information for Business Card

Daniel Ashcombe
Managing Director
Harbourne Vista Audio Marine Ltd

Requirements
Must have
• Office: 01632 960482
Mobile: 07700 900317
daniel@harbournevistaaudio.co.uk
www.harbournevistaaudio.co.uk

```html
<!DOCTYPE html>
<html lang="en">
<head>
<meta charset="utf-8">
<title>Harbourne Vista Audio Marine Ltd – Business Card</title>
<link rel="stylesheet" href="https://fonts.googleapis.com/css2?family=Exo+2:wght@600;700&display=swap">
<style>
  :root {
    --backdrop: #3b2119;
    --card-white: #ffffff;
    --sky-top: #a3d0e6;
    --sky-bottom: #86bcd9;
    --sea-top: #4f93bd;
    --sea-bottom: #2d74a1;
    --band-top: #92c3df;
    --band-bottom: #5e9fc7;
    --brand-blue: #1ba6e0;
    --ink: #111111;
    --white: #ffffff;
  }
  * { margin: 0; padding: 0; box-sizing: border-box; }
  html, body { width: 900px; height: 1200px; overflow: hidden; }
  body {
    background: var(--backdrop);
    position: relative;
    font-family: "Exo 2", sans-serif;
  }
  .card {
    position: absolute;
    left: 175px;
    width: 513px;
    height: 337px;
    background: var(--card-white);
    overflow: hidden;
    box-shadow: 0 4px 10px rgba(0,0,0,0.5);
  }
  .card--front { top: 204px; }
  .card--back { top: 588px; }

  .front__sky {
    position: absolute; left: 0; top: 0; width: 100%; height: 66px;
    background: linear-gradient(var(--sky-top), var(--sky-bottom));
  }
  .front__sea {
    position: absolute; left: 0; bottom: 0; width: 100%; height: 99px;
    background: linear-gradient(var(--sea-top), var(--sea-bottom));
  }
  .brand {
    position: absolute;
    display: flex;
    align-items: center;
  }
  .brand__dot {
    border-radius: 50%;
    background: var(--brand-blue);
    flex: none;
  }
  .brand__name {
    color: var(--brand-blue);
    font-weight: 700;
    line-height: 1.05;
  }
  .brand--large { left: 78px; top: 106px; gap: 18px; }
  .brand--large .brand__dot { width: 110px; height: 110px; }
  .brand--large .brand__line1 { display: block; font-size: 34px; }
  .brand--large .brand__line2 { display: block; font-size: 19px; }

  .back__band {
    position: absolute; left: 0; top: 85px; width: 100%; height: 166px;
    background: linear-gradient(var(--band-top), var(--band-bottom));
  }
  .brand--small { left: 26px; top: 48px; gap: 5px; }
  .brand--small .brand__dot { width: 26px; height: 26px; }
  .brand--small .brand__line1 { display: block; font-size: 12px; }
  .brand--small .brand__line2 { display: block; font-size: 7px; }

  .person__name {
    position: absolute; left: 133px; top: 116px;
    font-size: 42px; font-weight: 700; color: var(--white);
    letter-spacing: 0.5px; white-space: nowrap;
  }
  .person__role {
    position: absolute; left: 158px; top: 167px;
    font-size: 21px; font-weight: 700; color: var(--white);
    white-space: nowrap;
  }
  .contact {
    position: absolute; left: 16px; top: 257px;
    font-size: 12.5px; font-weight: 700; color: var(--ink);
    line-height: 16.5px; list-style: none;
  }
  .website {
    position: absolute; left: 180px; top: 310px;
    font-size: 12.5px; font-weight: 700; color: var(--ink);
  }
</style>
</head>
<body>
  <section class="card card--front">
    <div class="front__sky"></div>
    <div class="front__sea"></div>
    <div class="brand brand--large">
      <span class="brand__dot"></span>
      <span class="brand__name">
        <span class="brand__line1">Harbourne Vista</span>
        <span class="brand__line2">Audio Marine Ltd</span>
      </span>
    </div>
  </section>

  <section class="card card--back">
    <div class="brand brand--small">
      <span class="brand__dot"></span>
      <span class="brand__name">
        <span class="brand__line1">Harbourne Vista</span>
        <span class="brand__line2">Audio Marine Ltd</span>
      </span>
    </div>
    <div class="back__band"></div>
    <h1 class="person__name">Daniel Ashcombe</h1>
    <p class="person__role">Managing Director</p>
    <ul class="contact">
      <li>Office: 01632 960482</li>
      <li>Mobile: 07700 900317</li>
      <li>daniel@harbournevistaaudio.co.uk</li>
    </ul>
    <p class="website">www.harbournevistaaudio.co.uk</p>
  </section>
</body>
</html>
```